Business and Success Coaching Business Card

Need a business card for my coaching business. I coach small businesses, career professionals and, individuals wanting to unlock their human potential and achieve excellence. At the heart of our methodology is the Shaping Purposeful Action Routines Knowingly (SPARK) approach to formulate empowerment, create principles for success and setting achievable outcomes. I would like something that incorporates our new logo, something clean and sharp with a solid darker, but complementary background, color on the card front. The back should be white where there will be room for three questions

Target Market(s)

People looking to advance and improve themselves through a success coach

Industry/Entity Type

Life Coaching

Contact Information for Business Card

Contact information on card.
Business name on front of card
Questions on back

Font styles to use
Other font styles liked:
• Century Gothic or other Serif style fonts that look similar to Century Gothic

Colors

Designer to choose colors to be used in the design.

Requirements
Must have
• Logo on front of card
• Business name - The Steady Forge
• Contact name - Ted Harlow
• Address - Box 4619, Littleton, CO 80127-4619
• Phone number - 303-555-0147
• Email address - harlow.ted@thesteadyforge.example
• Certifications - CSC, CCHt, PTT, PNLP
• Back of card
• Three questions on the back of the card:
• If you were at your best, what would you do right now?
• What is the decision you have been avoiding?
• What's one action you could take in the next 10 minutes?
Nice to have
• I would like to see a solid color on the front of the card that compliments the logo.
• Back should be white, or could be contrasting, but need to have the three questions.

```html
<!DOCTYPE html>
<html lang="en">
<head>
<meta charset="utf-8">
<title>The Steady Forge – Business Card</title>
<link rel="stylesheet" href="https://fonts.googleapis.com/css2?family=Montserrat:wght@400;500;700&family=Open+Sans:ital,wght@0,600;1,600&display=swap">
<style>
  :root {
    --navy: #13306d;
    --navy-deep: #0f285c;
    --sky: #2b8ff0;
    --white: #ffffff;
    --ink: #1d3566;
    --backdrop: #e9e7e4;
    --ray: #c9d3e2;
  }
  * { box-sizing: border-box; margin: 0; padding: 0; }
  html, body {
    width: 1200px; height: 800px; overflow: hidden;
    background: var(--backdrop);
  }
  .stage {
    position: relative; width: 1200px; height: 800px;
    display: flex; align-items: center; justify-content: center; gap: 40px;
  }
  .card {
    position: relative; width: 540px; height: 309px; overflow: hidden;
    border-radius: 3px;
    box-shadow: 0 6px 18px rgba(0,0,0,.18);
  }

  /* Front */
  .card-front {
    background: var(--navy);
    color: var(--white);
    font-family: "Open Sans", sans-serif;
    text-align: center;
    padding-top: 62px;
  }
  .brand {
    display: inline-flex; align-items: center; gap: 12px;
    font-weight: 600; font-size: 38px; letter-spacing: -0.5px;
    color: var(--white);
  }
  .brand-mark {
    width: 16px; height: 16px; border-radius: 50%;
    background: var(--sky);
  }
  .tagline {
    margin-top: 2px;
    font-style: italic; font-weight: 600; font-size: 22px;
    color: var(--sky);
  }
  .questions {
    list-style: none; margin-top: 22px;
    font-size: 16.5px; line-height: 1.35; font-weight: 600;
  }

  /* Back */
  .card-back {
    background: var(--white);
    font-family: "Montserrat", sans-serif;
    color: var(--ink);
  }
  .contact {
    position: absolute; left: 44px; top: 60px;
    font-size: 14px; line-height: 1.45; font-weight: 500;
  }
  .contact-name {
    font-weight: 700; font-size: 17px; letter-spacing: .4px;
    color: var(--sky); text-transform: uppercase;
  }
  .credentials { margin-bottom: 12px; }
  .address { margin-bottom: 8px; }
  .contact-line { display: flex; align-items: center; gap: 7px; }
  .contact-line svg { width: 13px; height: 13px; fill: var(--sky); flex: none; }
  .back-band {
    position: absolute; left: 0; bottom: 0; width: 100%; height: 120px;
  }
  .back-brand {
    position: absolute; right: 34px; bottom: 34px;
    display: flex; align-items: center; gap: 10px;
    font-family: "Open Sans", sans-serif; font-weight: 600; font-size: 22px;
    color: var(--white);
  }
  .back-brand .brand-mark { width: 12px; height: 12px; }
</style>
</head>
<body>
<main class="stage">
  <section class="card card-front" aria-label="Card front">
    <div class="brand"><span class="brand-mark"></span>The Steady Forge</div>
    <p class="tagline">Jump-start your next phase</p>
    <ul class="questions">
      <li>If you were at your best, what would you do right now?</li>
      <li>What is the decision you have been avoiding?</li>
      <li>What's one action you could take in the next 10 minutes?</li>
    </ul>
  </section>

  <section class="card card-back" aria-label="Card back">
    <div class="contact">
      <p class="contact-name">Ted Harlow</p>
      <p class="credentials">CSC, CCHt, PTT, PNLP</p>
      <p>Box 4619</p>
      <p class="address">Littleton, CO 80127-4619</p>
      <p class="contact-line">
        <svg viewBox="0 0 24 24" aria-hidden="true"><path d="M6.6 10.8a15.1 15.1 0 0 0 6.6 6.6l2.2-2.2a1 1 0 0 1 1-.25 11.4 11.4 0 0 0 3.6.57 1 1 0 0 1 1 1V20a1 1 0 0 1-1 1A17 17 0 0 1 3 4a1 1 0 0 1 1-1h3.5a1 1 0 0 1 1 1c0 1.25.2 2.45.57 3.57a1 1 0 0 1-.25 1z"/></svg>
        303-555-0147
      </p>
      <p class="contact-line">
        <svg viewBox="0 0 24 24" aria-hidden="true"><path d="M2 5h20v14H2zm2 2v.5l8 5 8-5V7zm0 2.9V17h16V9.9l-8 5z"/></svg>
        harlow.ted@thesteadyforge.example
      </p>
    </div>
    <svg class="back-band" viewBox="0 0 540 120" preserveAspectRatio="none" aria-hidden="true">
      <path d="M170 120 C240 70 300 40 380 48 C440 54 490 40 540 30 L540 120 Z" fill="var(--navy)"/>
    </svg>
    <div class="back-brand"><span class="brand-mark"></span>The Steady Forge</div>
  </section>
</main>
</body>
</html>
```